Business Card, Stationary, and Invoice
PuzzleHarbor
Business Card, Stationary, and Invoice - Games
Creative Brief
Use specific fonts
Use logo font..or similar if logo font doesn't look good.
Bright & Fun-filled
Lyle Ostrand
Owner
84 Brackett Lane Monroe, NY 10953
lyle@puzzleharbor-example.com
www.puzzleharbor-example.com
Require business card, stationary, and invoice.

```html
<!DOCTYPE html>
<html lang="en">
<head>
<meta charset="utf-8">
<title>PuzzleHarbor Stationery Set</title>
<link href="https://fonts.googleapis.com/css2?family=Cinzel:wght@700&family=Lato:wght@400;700&display=swap" rel="stylesheet">
<style>
:root{
  --bg:#ececec;
  --paper:#ffffff;
  --gold:#b39a63;
  --gold-dark:#8f7a4a;
  --ink:#1e1b17;
  --muted:#8a8a8a;
  --shadow:0 1px 3px rgba(0,0,0,.25);
}
*{margin:0;padding:0;box-sizing:border-box}
html,body{width:1200px;height:310px;overflow:hidden;background:var(--bg)}
body{position:relative;font-family:"Lato",sans-serif;color:var(--ink)}
.piece{position:absolute;background:var(--paper);box-shadow:var(--shadow);overflow:hidden}
.brand{font-family:"Cinzel",serif;font-weight:700;color:var(--ink);white-space:nowrap;display:flex;align-items:center;gap:4px}
.brand .dot{border-radius:50%;background:var(--ink);display:inline-block}
.brand.light{color:var(--ink)}
.band{position:absolute;left:0;right:0;top:0;background:var(--gold)}
.tiny{font-size:4px;line-height:1.4;color:var(--ink)}
.caption{position:absolute;font-size:5px;color:var(--muted);text-align:center}

/* logo block */
.logo-block{position:absolute;left:12px;top:20px;width:165px}
.logo-block .brand{font-size:21px;gap:6px}
.logo-block .brand .dot{width:14px;height:14px;background:var(--gold)}
.logo-block .tagline{font-size:7px;letter-spacing:1px;color:var(--gold-dark);margin:4px 0 0 20px}

/* cards */
.card-front{left:12px;top:150px;width:168px;height:52px}
.card-front .band{height:16px}
.card-front .brand{position:absolute;left:6px;top:4px;font-size:9px}
.card-front .brand .dot{width:6px;height:6px}
.card-front .details{position:absolute;left:90px;top:22px}
.card-back{left:12px;top:211px;width:125px;height:58px}
.card-back .brand{position:absolute;left:22px;top:22px;font-size:10px}
.card-back .brand .dot{width:7px;height:7px;background:var(--gold)}
.card-gold{left:144px;top:211px;width:125px;height:58px;background:var(--gold)}
.card-gold .brand{position:absolute;left:22px;top:22px;font-size:10px}
.card-gold .brand .dot{width:7px;height:7px}

/* letterhead */
.letterhead{top:17px;width:197px;height:275px}
.letterhead .band{height:22px}
.letterhead .brand{position:absolute;left:8px;top:5px;font-size:10px}
.letterhead .brand .dot{width:7px;height:7px}
.letterhead .contact{position:absolute;right:6px;top:8px;text-align:right;font-size:3.5px}
.letterhead .footer{position:absolute;left:0;right:0;bottom:6px;text-align:center;font-size:3.5px;color:var(--muted)}
.lh-1{left:276px}
.lh-2{left:492px}

/* compliment slips */
.slip{left:701px;width:192px;height:112px}
.slip .band{height:18px}
.slip .brand{position:absolute;left:8px;top:24px;font-size:9px}
.slip .brand .dot{width:6px;height:6px;background:var(--gold)}
.slip .footer{position:absolute;left:0;right:0;bottom:5px;text-align:center;font-size:3.5px;color:var(--muted)}
.slip-1{top:43px}
.slip-2{top:180px}

/* envelopes */
.envelope{left:910px;width:272px;height:72px}
.envelope svg{position:absolute;inset:0}
.envelope .brand{position:absolute;left:50%;transform:translateX(-50%);font-size:9px}
.envelope .brand .dot{width:6px;height:6px;background:var(--gold)}
.env-dark{top:42px;background:var(--ink)}
.env-dark .brand{top:38px;color:var(--gold)}
.env-gold{top:118px}
.env-gold .brand{top:42px}
.env-plain{top:196px}
.env-plain .brand{top:42px}
</style>
</head>
<body>

<div class="logo-block">
  <div class="brand"><span class="dot"></span>PuzzleHarbor</div>
  <div class="tagline">TQW PLAYWORKS</div>
</div>

<div class="piece card-front">
  <div class="band"></div>
  <div class="brand"><span class="dot"></span>PuzzleHarbor</div>
  <div class="details tiny">
    <strong>Lyle Ostrand</strong> · Owner<br>
    84 Brackett Lane Monroe, NY 10953<br>
    lyle@puzzleharbor-example.com<br>
    www.puzzleharbor-example.com
  </div>
</div>

<div class="piece card-back">
  <div class="brand"><span class="dot"></span>PuzzleHarbor</div>
</div>
<div class="piece card-gold">
  <div class="brand"><span class="dot"></span>PuzzleHarbor</div>
</div>
<div class="caption" style="left:12px;top:276px;width:257px">Business Cards</div>

<div class="piece letterhead lh-1">
  <div class="band"></div>
  <div class="brand"><span class="dot"></span>PuzzleHarbor</div>
  <div class="contact tiny">84 Brackett Lane Monroe, NY 10953<br>www.puzzleharbor-example.com</div>
  <div class="footer">84 Brackett Lane Monroe, NY 10953 · lyle@puzzleharbor-example.com · www.puzzleharbor-example.com</div>
</div>
<div class="caption" style="left:276px;top:297px;width:197px">Letterhead</div>

<div class="piece letterhead lh-2">
  <div class="band"></div>
  <div class="brand"><span class="dot"></span>PuzzleHarbor</div>
  <div class="contact tiny">84 Brackett Lane Monroe, NY 10953<br>www.puzzleharbor-example.com</div>
  <div class="footer">84 Brackett Lane Monroe, NY 10953 · lyle@puzzleharbor-example.com · www.puzzleharbor-example.com</div>
</div>
<div class="caption" style="left:492px;top:297px;width:197px">Letterhead</div>

<div class="piece slip slip-1">
  <div class="band"></div>
  <div class="brand"><span class="dot"></span>PuzzleHarbor</div>
  <div class="footer">84 Brackett Lane Monroe, NY 10953 · www.puzzleharbor-example.com</div>
</div>
<div class="caption" style="left:701px;top:158px;width:192px">Compliment Slip</div>

<div class="piece slip slip-2">
  <div class="band"></div>
  <div class="brand"><span class="dot"></span>PuzzleHarbor</div>
  <div class="footer">84 Brackett Lane Monroe, NY 10953 · www.puzzleharbor-example.com</div>
</div>

<div class="piece envelope env-dark">
  <svg viewBox="0 0 272 72" preserveAspectRatio="none"><polygon points="0,0 272,0 136,30" fill="#2c2822"/></svg>
  <div class="brand"><span class="dot"></span>PuzzleHarbor</div>
</div>
<div class="piece envelope env-gold">
  <svg viewBox="0 0 272 72" preserveAspectRatio="none"><polygon points="0,0 272,0 136,32" fill="#b39a63"/></svg>
  <div class="brand"><span class="dot"></span>PuzzleHarbor</div>
</div>
<div class="piece envelope env-plain">
  <svg viewBox="0 0 272 72" preserveAspectRatio="none"><polyline points="0,0 136,32 272,0" fill="none" stroke="#d6d6d6" stroke-width="1"/></svg>
  <div class="brand"><span class="dot"></span>PuzzleHarbor</div>
</div>
<div class="caption" style="left:910px;top:274px;width:272px">Envelopes</div>

</body>
</html>
```